Talbrin Business Cards

Front and back. Simon Kavelle MBA is the CEO of Talbrin Homes. Black white and grays. Logo and cool design.

Target Market(s)

Professional lenders and investors

Industry/Entity Type

Real estate developer. NO HOUSES OR ROOFS

Contact Information for Business Card

Logo, name and unique design. Front and back. Simon Kavelle MBA is the CEO of Talbrin Homes. Black white and grays. Logo and cool design.

Font styles to use
Sans Serif

Colors

Designer to choose only greyscale colors for use in the design.

Requirements
Must have
• Cool look. Not the same card I could design.
Nice to have
• Something memorable
Should not have
• Basic

```html
<!DOCTYPE html>
<html lang="en">
<head>
<meta charset="UTF-8">
<title>Talbrin Homes — Business Cards</title>
<link href="https://fonts.googleapis.com/css2?family=Poppins:wght@400;600;700&display=swap" rel="stylesheet">
<style>
  :root{
    --stage:#2d2d2d;
    --card:#000000;
    --ink:#ffffff;
    --rule:#d9d9d9;
  }
  *{margin:0;padding:0;box-sizing:border-box}
  html,body{width:1200px;height:1015px;overflow:hidden}
  body{background:var(--stage);font-family:'Poppins',sans-serif;color:var(--ink);position:relative}
  .card{
    position:absolute;left:250px;width:700px;height:400px;
    background:var(--card);
    box-shadow:0 14px 30px rgba(0,0,0,.45);
    overflow:hidden;
  }
  .card--front{top:85px}
  .card--back{top:530px}
  .wordmark{font-weight:700;color:var(--ink);letter-spacing:-1px;line-height:1;white-space:nowrap}
  .card--front .wordmark{position:absolute;left:50%;top:50%;transform:translate(-50%,-50%);font-size:74px}
  .card--back .wordmark{position:absolute;right:48px;top:52px;font-size:50px}
  .contact{position:absolute;left:58px;top:150px;width:320px}
  .contact__name{font-weight:700;font-size:22px;line-height:1.1}
  .contact__title{font-weight:400;font-size:16px;line-height:1.3;margin-top:2px}
  .contact__rule{width:135px;height:1px;background:var(--rule);margin:14px 0}
  .contact__list{list-style:none}
  .contact__item{display:flex;align-items:center;gap:8px;font-size:16px;line-height:1.45}
  .contact__icon{width:15px;height:15px;flex:none}
  .contact__address{font-size:16px;line-height:1.35}
</style>
</head>
<body>
  <section class="card card--front">
    <div class="wordmark">Talbrin Homes</div>
  </section>

  <section class="card card--back">
    <div class="wordmark">Talbrin Homes</div>
    <div class="contact">
      <div class="contact__name">Simon Kavelle, MBA</div>
      <div class="contact__title">Chief Executive Officer</div>
      <div class="contact__rule"></div>
      <ul class="contact__list">
        <li class="contact__item">
          <svg class="contact__icon" viewBox="0 0 24 24" fill="#fff"><path d="M6.6 10.8a15 15 0 0 0 6.6 6.6l2.2-2.2a1 1 0 0 1 1-.25 11.4 11.4 0 0 0 3.6.57 1 1 0 0 1 1 1V20a1 1 0 0 1-1 1A17 17 0 0 1 3 4a1 1 0 0 1 1-1h3.5a1 1 0 0 1 1 1c0 1.25.2 2.45.57 3.57a1 1 0 0 1-.25 1z"/></svg>
          044-555 018 274
        </li>
        <li class="contact__item">
          <svg class="contact__icon" viewBox="0 0 24 24" fill="none" stroke="#fff" stroke-width="2"><rect x="2" y="5" width="20" height="14"/><path d="M2 5l10 8 10-8"/></svg>
          info@talbrinhomes.com
        </li>
        <li class="contact__item">
          <svg class="contact__icon" viewBox="0 0 24 24" fill="none" stroke="#fff" stroke-width="2"><circle cx="12" cy="12" r="10"/><path d="M2 12h20M12 2c3 3 3 17 0 20M12 2c-3 3-3 17 0 20"/></svg>
          www.talbrinhomes.com
        </li>
      </ul>
      <div class="contact__rule"></div>
      <p class="contact__address">87, Orland Quay Road<br>30918, Northmere</p>
    </div>
  </section>
</body>
</html>
```